I’d like to see something with similar colors and design concept to the “Your Fortune Starts at Breakfast” book included in attchment

Create a book cover with front cover, and full front, spine and back cover spread.
Simple and clean design. See design inspiration below.
Size 6X9
Title of the book: Write Onward! Veteran Editors Reveal Their Methods

Please leave space for 6 authors names on the front cover. Authors names will be provided at a later time.

Back of book should included the name of the publishing company:
Bright Lantern Publishing

As well as the following synopsis
The landscape of the publishing industry is changing. Gone are the days of coveted gatekeepers controlling content and dictating the messages being distributed. With the rise of technology, social media , self-publishing platforms, and independent bookstores, there are increased opportunities for people to share their ideas, messages, and stories with the world through books. The types of books that we’re publishing are also evolving — mini-books, audio books, journals, multi-author books, cook books, children’s books, comic books, coloring books, interactive books, tarot and oracle card decks are all expanding the podium for people to express ideas and influence the culture. More and more entrepreneurs are posturing themselves as thought leaders by leveraging this growing platform.
But that doesn't mean it’s easy.
Even with the expanding platforms and opportunities, only a fraction of people with publishing ambitions are able to achieve this coveted dream held by so many. It can be a daunting process for budding authors trying to maneuver through the writing, packaging, marketing, and publishing processes alone.

In this book you'll find passionate, purpose-driven, and well-versed experts working in the various areas of publishing, eager to help open your eyes to the promise of publishing and effortlessly guide you through the process.

Colors
0094D4
00A9DD
6FCCEA
C7EBF8
E9F6FB
FFF300
FFF600
FEFA6F
FFFEC7
FFFEE8
FFC000
F8CF3A
FAE287
FDF2CF
FEFAEE
F0912C
F2A743
F7CA91
FBE8D2
FDF5EE
EE7325
F08F49
F5BC92
FAE3D3
FDF4ED
6B429C
8869AF
B7A5CE
E3DAEB
F3F0F8

```html
<!DOCTYPE html>
<html lang="en">
<head>
<meta charset="utf-8">
<title>Write Onward! Veteran Editors Reveal Their Methods: Cover Spread</title>
<link rel="stylesheet" href="https://fonts.googleapis.com/css2?family=Abel&family=Quicksand:wght@300;400;500;700&display=swap">
<style>
  :root {
    --stage: #333333;
    --sheet: #ffffff;
    --paper: #dfdbd4;
    --rust: #a8604f;
    --rust-deep: #b0502e;
    --brown: #3d140c;
    --sage: #6d8c84;
    --teal: #155a61;
    --spine-rust: #a55c4a;
    --spine-sage: #9dbbb1;
    --spine-rust-light: #c8775c;
    --body: #2b2420;
  }
  * { margin: 0; padding: 0; box-sizing: border-box; }
  html, body { width: 1200px; height: 1177px; overflow: hidden; background: var(--stage); }
  .canvas { position: relative; width: 1200px; height: 1177px; background: var(--stage); }
  .sheet { position: absolute; left: 80px; top: 223px; width: 1038px; height: 718px; background: var(--sheet); }

  .panel { position: absolute; top: 244px; height: 675px; background: var(--paper); }
  .back { left: 102px; width: 438px; }
  .front { left: 660px; width: 440px; }
  .spine { position: absolute; left: 559px; top: 244px; width: 81px; height: 675px; }

  .title-art { position: absolute; display: block; overflow: visible; }
  .title-art text { font-family: "Quicksand", sans-serif; }
  .t-main { fill: var(--rust); font-weight: 300; }
  .t-sub { fill: var(--brown); font-weight: 700; }
  .t-line1 { fill: var(--sage); font-weight: 300; }
  .t-line2 { fill: var(--teal); font-weight: 400; }
  .t-line3 { fill: var(--rust-deep); font-weight: 400; }
  .dots { stroke: var(--teal); stroke-width: 4; stroke-linecap: round; stroke-dasharray: 0 8.2; }
  .dots-front { stroke: var(--sage); }

  .front-publisher { position: absolute; left: 0; top: 12px; width: 100%; text-align: center;
    font-family: "Quicksand", sans-serif; font-weight: 500; font-size: 16px; color: var(--brown); }
  .authors { position: absolute; left: 0; top: 572px; width: 100%; text-align: center;
    font-family: "Quicksand", sans-serif; font-weight: 400; font-size: 14.5px; line-height: 18px;
    letter-spacing: 0.2px; color: var(--brown); }
  .authors .a-rust { color: var(--rust); }
  .authors .a-sage { color: var(--sage); }

  .frame { position: absolute; left: 60px; top: 16px; width: 324px; height: 286px; border: 2px solid var(--sheet); }
  .synopsis { position: absolute; left: 22px; top: 335px; width: 394px;
    font-family: "Abel", sans-serif; font-size: 10.3px; line-height: 14.6px; color: var(--body);
    text-align: justify; }
  .synopsis p + p { margin-top: 14.6px; }
  .synopsis .closing { color: var(--teal); font-size: 10.8px; }
  .back-publisher { position: absolute; left: 22px; top: 648px;
    font-family: "Abel", sans-serif; font-size: 12px; color: var(--rust-deep); }
  .barcode-box { position: absolute; left: 274px; top: 636px; width: 128px; height: 34px;
    background: var(--sheet); border: 1px solid var(--teal);
    display: flex; align-items: center; justify-content: center;
    font-family: "Abel", sans-serif; font-size: 10px; color: var(--body); }

  .spine-top { position: absolute; left: 0; top: 0; width: 81px; height: 314px; background: var(--teal); }
  .spine-mid { position: absolute; left: 0; top: 314px; width: 81px; height: 314px; background: var(--brown); }
  .spine-foot { position: absolute; left: 0; top: 628px; width: 81px; height: 47px; background: var(--spine-rust);
    display: flex; align-items: center; justify-content: center; text-align: center;
    font-family: "Abel", sans-serif; font-size: 10px; line-height: 11px; color: var(--sheet); }
  .spine-art { position: absolute; left: 0; top: 0; display: block; }
  .spine-art text { font-family: "Quicksand", sans-serif; fill: var(--sheet); }
  .spine-title { font-weight: 300; }
  .spine-subtitle { font-weight: 400; }
  .spine-subtitle .s-sage { fill: var(--spine-sage); }
  .spine-subtitle .s-rust { fill: var(--spine-rust-light); }
</style>
</head>
<body>
<main class="canvas">
  <div class="sheet"></div>

  <section class="panel back" aria-label="Back cover">
    <div class="frame"></div>
    <svg class="title-art" style="left:0;top:0" width="438" height="320" viewBox="0 0 438 320" aria-label="Write Onward! Veteran Editors Reveal Their Methods">
      <text class="t-main" x="108" y="114" font-size="97" textLength="228" lengthAdjust="spacingAndGlyphs">WRITE</text>
      <text class="t-sub" x="108" y="162" font-size="41" textLength="224" lengthAdjust="spacingAndGlyphs">ONWARD!</text>
      <line class="dots" x1="110" y1="174" x2="330" y2="174"/>
      <text class="t-line1" x="110" y="210" font-size="29" textLength="224" lengthAdjust="spacingAndGlyphs">VETERAN EDITORS</text>
      <text class="t-line2" x="110" y="248" font-size="45" textLength="224" lengthAdjust="spacingAndGlyphs">REVEAL THEIR</text>
      <text class="t-line3" x="110" y="284" font-size="41" textLength="220" lengthAdjust="spacing">METHODS</text>
    </svg>
    <div class="synopsis">
      <p>The landscape of the publishing industry is changing. Gone are the days of coveted gatekeepers controlling content and dictating the messages being distributed. With the rise of technology, social media , self-publishing platforms, and independent bookstores, there are increased opportunities for people to share their ideas, messages, and stories with the world through books. The types of books that we’re publishing are also evolving — mini-books, audio books, journals, multi-author books, cook books, children’s books, comic books, coloring books, interactive books, tarot and oracle card decks are all expanding the podium for people to express ideas and influence the culture. More and more entrepreneurs are posturing themselves as thought leaders by leveraging this growing platform.</p>
      <p>But that doesn't mean it’s easy.<br>Even with the expanding platforms and opportunities, only a fraction of people with publishing ambitions are able to achieve this coveted dream held by so many. It can be a daunting process for budding authors trying to maneuver through the writing, packaging, marketing, and publishing processes alone.</p>
      <p class="closing">In this book you'll find passionate, purpose-driven, and well-versed experts working in the various areas of publishing, eager to help open your eyes to the promise of publishing and effortlessly guide you through the process.</p>
    </div>
    <div class="back-publisher">Bright Lantern Publishing</div>
    <div class="barcode-box">BARCODE</div>
  </section>

  <section class="spine" aria-label="Spine">
    <div class="spine-top">
      <svg class="spine-art" width="81" height="314" viewBox="0 0 81 314">
        <text class="spine-title" transform="translate(29,22) rotate(90)" font-size="31" textLength="262" lengthAdjust="spacingAndGlyphs">WRITE ONWARD!</text>
      </svg>
    </div>
    <div class="spine-mid">
      <svg class="spine-art" width="81" height="314" viewBox="0 0 81 314">
        <text class="spine-subtitle" transform="translate(35,14) rotate(90)" font-size="15" textLength="286" lengthAdjust="spacingAndGlyphs">VETERAN EDITORS <tspan class="s-sage">REVEAL THEIR</tspan> <tspan class="s-rust">METHODS</tspan></text>
      </svg>
    </div>
    <div class="spine-foot">Bright<br>Lantern<br>Publishing</div>
  </section>

  <section class="panel front" aria-label="Front cover">
    <div class="front-publisher">Bright Lantern Publishing</div>
    <svg class="title-art" style="left:0;top:0" width="440" height="560" viewBox="0 0 440 560" aria-label="Write Onward! Veteran Editors Reveal Their Methods">
      <text class="t-main" x="22" y="197" font-size="146" textLength="400" lengthAdjust="spacingAndGlyphs">WRITE</text>
      <text class="t-sub" x="22" y="279" font-size="73" textLength="396" lengthAdjust="spacingAndGlyphs">ONWARD!</text>
      <line class="dots" x1="24" y1="331" x2="420" y2="331"/>
      <text class="t-line1" x="24" y="396" font-size="53" textLength="396" lengthAdjust="spacingAndGlyphs">VETERAN EDITORS</text>
      <text class="t-line2" x="22" y="464" font-size="66" textLength="398" lengthAdjust="spacingAndGlyphs">REVEAL THEIR</text>
      <text class="t-line3" x="22" y="527" font-size="69" textLength="398" lengthAdjust="spacing">METHODS</text>
      <line class="dots dots-front" x1="24" y1="549" x2="420" y2="549"/>
    </svg>
    <div class="authors">
      AUTHOR NAME SURNAME 1 • <span class="a-rust">AUTHOR NAMESURNAME 2</span> •<br>
      <span class="a-sage">AUTHOR NAME SURNAME 3</span> • AUTHOR NAME SURNAME 4 •<br>
      AUTHOR NAME SURNAME 5 • <span class="a-rust">AUTHOR NAME SURNAME 6</span> •
    </div>
  </section>
</main>
</body>
</html>
```